Yard Sign Design Needed

Yard sign needed for mowing & landscaping company. Would like to use the top logo with black background which is attached. Would like MOWING to be in large standout letters. The word "landscaping" can be smaller and more artistic or omitted. Will need room for phone number once design is approved. The phone number will need to stand out and look identical/similar to the word 'MOWING"

```html
<!DOCTYPE html>
<html lang="en">
<head>
<meta charset="utf-8">
<title>Braxen Contractors LLC – Mowing &amp; Landscaping Yard Sign</title>
<link rel="stylesheet" href="https://fonts.googleapis.com/css2?family=Russo+One&family=Pinyon+Script&family=Archivo+Black&display=swap">
<style>
  :root {
    --sign-black: #000000;
    --olive: #8ea60b;
    --olive-dark: #7c8f08;
    --lime: #c5f06a;
    --lime-pale: #eaf8d0;
    --white: #ffffff;
    --ink: #050505;
  }
  * { margin: 0; padding: 0; box-sizing: border-box; }
  html, body {
    width: 1200px;
    height: 902px;
    overflow: hidden;
    background: var(--sign-black);
  }
  .yard-sign {
    position: relative;
    width: 1200px;
    height: 902px;
    background: var(--sign-black);
    overflow: hidden;
  }

  /* Company brand block */
  .brand {
    position: absolute;
    left: 198px;
    top: 60px;
    display: flex;
    align-items: center;
    gap: 62px;
  }
  .brand-mark {
    width: 200px;
    height: 200px;
    background: var(--olive);
    flex: none;
  }
  .brand-name {
    font-family: "Russo One", sans-serif;
    color: var(--olive);
    text-align: center;
    line-height: 1;
    width: 530px;
  }
  .brand-name .name-main {
    display: block;
    font-size: 94px;
    letter-spacing: 2px;
  }
  .brand-name .name-sub {
    display: block;
    font-size: 47px;
    letter-spacing: 1px;
    margin-top: 18px;
  }
  .brand-name .name-legal {
    display: flex;
    align-items: center;
    gap: 18px;
    font-size: 30px;
    margin-top: 6px;
  }
  .brand-name .name-legal::before,
  .brand-name .name-legal::after {
    content: "";
    flex: 1;
    height: 2px;
    background: var(--white);
  }

  /* Headline service */
  .service-main {
    position: absolute;
    left: 0;
    width: 1200px;
    top: 392px;
    text-align: center;
    font-family: "Russo One", sans-serif;
    font-size: 178px;
    line-height: 1;
    letter-spacing: 4px;
    background: linear-gradient(90deg, var(--white) 10%, var(--lime) 40%, #a9cf3a 65%, var(--olive-dark) 92%);
    -webkit-background-clip: text;
    background-clip: text;
    color: transparent;
  }

  .service-sub {
    position: absolute;
    left: 0;
    width: 1200px;
    top: 560px;
    text-align: center;
    font-family: "Pinyon Script", cursive;
    font-size: 150px;
    line-height: 1.1;
    color: var(--white);
  }

  /* Contact band */
  .contact-band {
    position: absolute;
    left: 0;
    top: 744px;
    width: 1200px;
    height: 158px;
    background: linear-gradient(90deg, var(--white) 15%, var(--lime-pale) 55%, var(--lime) 100%);
  }
  .phone-badge {
    position: absolute;
    left: -82px;
    top: -4px;
    width: 202px;
    height: 202px;
    border-radius: 50%;
    background: var(--olive);
    display: flex;
    align-items: center;
    justify-content: flex-end;
    padding-right: 28px;
  }
  .phone-badge svg {
    width: 86px;
    height: 86px;
  }
  .phone-number {
    position: absolute;
    left: 140px;
    top: 22px;
    width: 1045px;
    font-family: "Archivo Black", sans-serif;
    font-size: 126px;
    line-height: 1;
    letter-spacing: 2px;
    color: var(--ink);
    white-space: nowrap;
  }
</style>
</head>
<body>
  <main class="yard-sign">
    <header class="brand">
      <div class="brand-mark" aria-hidden="true"></div>
      <h1 class="brand-name">
        <span class="name-main">BRAXEN</span>
        <span class="name-sub">CONTRACTORS</span>
        <span class="name-legal">LLC</span>
      </h1>
    </header>

    <h2 class="service-main">MOWING</h2>
    <p class="service-sub">Landscaping</p>

    <footer class="contact-band">
      <div class="phone-badge">
        <svg viewBox="0 0 24 24" aria-hidden="true">
          <path fill="#ffffff" d="M6.6 10.8c1.4 2.8 3.8 5.1 6.6 6.6l2.2-2.2c.3-.3.7-.4 1-.2 1.1.4 2.3.6 3.6.6.6 0 1 .4 1 1V20c0 .6-.4 1-1 1C10.6 21 3 13.4 3 4c0-.6.4-1 1-1h3.5c.6 0 1 .4 1 1 0 1.3.2 2.5.6 3.6.1.3 0 .7-.2 1L6.6 10.8z"/>
        </svg>
      </div>
      <p class="phone-number">047-5528-3190</p>
    </footer>
  </main>
</body>
</html>
```